Crestmoor Business Cards

I need a business card designed with the following information.

Company Name: Crestmoor Wealth Management
Name: BriAnne Tolvey
Title: Executive Assistant
Cell: (555) 302-7164
Direct Line: (555) 917-5082
Email: brianne@crestmoorwm.example
Address: 20537 W. Harwell PKWY Ste. B
Larkfield, CO 77512

I have attached the logo.
I would like it in navy blue and silver.
Thanks.

```html
<!DOCTYPE html>
<html lang="en">
<head>
<meta charset="UTF-8">
<title>Crestmoor Wealth Management – Business Card</title>
<link href="https://fonts.googleapis.com/css2?family=Tenor+Sans&display=swap" rel="stylesheet">
<style>
  :root {
    --backdrop: #3a3a3c;
    --navy: #18223d;
    --navy-light: #2a3658;
    --white: #ffffff;
    --silver: #d9dde6;
  }
  * { margin: 0; padding: 0; box-sizing: border-box; }
  html, body {
    width: 799px;
    height: 1200px;
    overflow: hidden;
    background: var(--backdrop);
    font-family: "Tenor Sans", sans-serif;
  }
  .card {
    position: absolute;
    left: 80px;
    width: 640px;
    height: 366px;
    background: var(--navy);
    overflow: hidden;
  }
  .card--front { top: 140px; }
  .card--back { top: 660px; }

  .front-mark {
    position: absolute;
    inset: 0;
    display: flex;
    align-items: center;
    justify-content: center;
    color: var(--navy-light);
    font-size: 40px;
    letter-spacing: 0.3em;
    padding-left: 0.3em;
  }

  .back-block {
    position: absolute;
    left: 0;
    top: 92px;
    width: 190px;
    height: 190px;
    background: var(--white);
  }

  .wordmark {
    position: absolute;
    right: 40px;
    top: 52px;
    text-align: right;
    color: var(--white);
  }
  .wordmark__name {
    font-size: 34px;
    letter-spacing: 0.32em;
    margin-right: -0.32em;
    line-height: 1;
  }
  .wordmark__tagline {
    font-size: 12.5px;
    letter-spacing: 0.26em;
    margin-right: -0.26em;
    margin-top: 4px;
  }

  .person {
    position: absolute;
    right: 40px;
    top: 142px;
    text-align: right;
    color: var(--white);
  }
  .person__name { font-size: 21px; letter-spacing: 0.03em; }
  .person__title { font-size: 12.5px; color: var(--silver); margin-top: 2px; }

  .contacts {
    position: absolute;
    right: 40px;
    top: 206px;
    list-style: none;
    color: var(--white);
    font-size: 14px;
  }
  .contacts li {
    display: flex;
    justify-content: flex-end;
    align-items: center;
    gap: 9px;
    line-height: 21px;
  }
  .contacts svg { width: 12px; height: 12px; fill: none; stroke: var(--white); stroke-width: 1.4; }

  .address {
    position: absolute;
    right: 40px;
    bottom: 26px;
    color: var(--white);
    font-size: 14px;
  }
</style>
</head>
<body>
  <section class="card card--front" aria-label="Card front">
    <div class="front-mark">CRESTMOOR</div>
  </section>

  <section class="card card--back" aria-label="Card back">
    <div class="back-block"></div>

    <div class="wordmark">
      <div class="wordmark__name">CRESTMOOR</div>
      <div class="wordmark__tagline">WEALTH MANAGEMENT</div>
    </div>

    <div class="person">
      <div class="person__name">BRIANNE TOLVEY</div>
      <div class="person__title">Executive Assistant</div>
    </div>

    <ul class="contacts">
      <li>(555) 302-7164
        <svg viewBox="0 0 12 12"><rect x="3" y="1" width="6" height="10" rx="1"/><line x1="5" y1="9" x2="7" y2="9"/></svg>
      </li>
      <li>(555) 917-5082
        <svg viewBox="0 0 12 12"><path d="M2 4c0-2 8-2 8 0v1H8V4H4v1H2z"/><rect x="3" y="6" width="6" height="4"/></svg>
      </li>
      <li>brianne@crestmoorwm.example
        <svg viewBox="0 0 12 12"><rect x="1" y="3" width="10" height="7"/><polyline points="1,3 6,7 11,3"/></svg>
      </li>
      <li>www.crestmoorwm.example
        <svg viewBox="0 0 12 12"><circle cx="6" cy="6" r="5"/><ellipse cx="6" cy="6" rx="2.2" ry="5"/><line x1="1" y1="6" x2="11" y2="6"/></svg>
      </li>
    </ul>

    <div class="address">20537 W. Harwell PKWY Ste. B Larkfield, CO 77512</div>
  </section>
</body>
</html>
```